Business Card for By Karel Voss

Looking to have a business card designed for my lifestyle and fitness company. My company offers personal training, online programming and nutrition advice based out of London, United Kingdom.

I'd like to see modern, sleek designs, focusing on black, matte black or matte grey. Design doesn't need to be overly descriptive as this will also be used as a personal business card. I've included my logo.

Please note that my company is no longer called "Fitness by Karel Voss" but instead "By Karel Voss", this is because of my other ventures. Therefore please don't use the "fitness by karel voss" text.

information about my company can be found at www.bykarelvoss.com

Company is also based out of London (United Kingdom) & Sydney (Australia) this could be reflected on the card.

Industry/Entity Type

Business

Contact Information for Business Card

Karel Voss
+44 7382 615027
karel@bykarelvoss.com
www.bykarelvoss.com

Font styles to use
Sans Serif

Requirements
Must have
• All contact details and inclusion of my logo.

```html
<!DOCTYPE html>
<html lang="en">
<head>
<meta charset="utf-8">
<title>By Karel Voss — Business Card</title>
<link href="https://fonts.googleapis.com/css2?family=Lato:wght@400;700;900&display=swap" rel="stylesheet">
<style>
  :root {
    --stage: #e9e7e4;
    --card-light: #ffffff;
    --card-dark: #151515;
    --ink: #111111;
    --ink-reverse: #ffffff;
  }
  * { margin: 0; padding: 0; box-sizing: border-box; }
  html, body {
    width: 1200px; height: 900px; overflow: hidden;
    background: var(--stage);
    font-family: "Lato", Arial, sans-serif;
  }
  .canvas { position: relative; width: 1200px; height: 900px; }

  .card { position: absolute; box-shadow: 0 6px 18px rgba(0,0,0,.18); overflow: hidden; }
  .card--front {
    left: 78px; top: 35px; width: 587px; height: 362px;
    background: var(--card-light); color: var(--ink);
  }
  .card--back {
    left: 388px; top: 505px; width: 567px; height: 352px;
    background: var(--card-dark); color: var(--ink-reverse);
  }

  .brand-mark {
    position: absolute; border-radius: 50%;
  }
  .card--front .brand-mark {
    left: 12px; top: 58px; width: 250px; height: 250px;
    background: var(--ink);
  }
  .card--back .brand-mark {
    left: 226px; top: 82px; width: 115px; height: 115px;
    background: var(--ink-reverse);
  }

  .brand-name {
    position: absolute;
    font-weight: 900; text-transform: uppercase; letter-spacing: 1px;
    white-space: nowrap;
  }
  .card--front .brand-name {
    right: 35px; top: 135px; font-size: 28px; color: var(--ink);
  }
  .card--back .brand-name {
    left: 0; right: 0; top: 243px; text-align: center;
    font-size: 28px; color: var(--ink-reverse);
  }

  .holder-name {
    position: absolute; right: 35px; top: 204px;
    font-size: 18px; font-weight: 900; letter-spacing: .6px;
    text-transform: uppercase;
  }

  .contact-list {
    position: absolute; right: 36px; top: 252px;
    list-style: none; text-align: right;
    font-size: 15px; line-height: 22px;
  }
  .contact-list li { display: flex; align-items: center; justify-content: flex-end; gap: 4px; }
  .contact-icon { width: 12px; height: 12px; fill: var(--ink); flex: none; }
</style>
</head>
<body>
<main class="canvas">

  <section class="card card--front" aria-label="Business card front">
    <div class="brand-mark" aria-hidden="true"></div>
    <p class="brand-name">By Karel Voss</p>
    <h1 class="holder-name">Karel Voss</h1>
    <ul class="contact-list">
      <li>+44 7382 615027
        <svg class="contact-icon" viewBox="0 0 12 12" aria-hidden="true">
          <path d="M1 4.5C1 3 2.5 2 6 2s5 1 5 2.5v1H8.5V4.3C7.8 4 4.2 4 3.5 4.3v1.2H1z"/>
          <rect x="2.5" y="6" width="7" height="4.5" rx="1"/>
        </svg>
      </li>
      <li>karel@bykarelvoss.com
        <svg class="contact-icon" viewBox="0 0 12 12" aria-hidden="true">
          <rect x="1" y="2.5" width="10" height="7.5" rx=".5"/>
          <path d="M1.5 3.2 6 6.8l4.5-3.6" fill="none" stroke="#fff" stroke-width="1"/>
        </svg>
      </li>
      <li>www.bykarelvoss.com
        <svg class="contact-icon" viewBox="0 0 12 12" aria-hidden="true">
          <circle cx="6" cy="6" r="5"/>
          <path d="M3 4.2c1.2 0 1.8.9 1.4 1.9-.4.9.4 1.6.2 2.8M7.5 2c-.3 1 .6 1.6 1.6 1.4.9-.2 1.1 1 .6 1.9" fill="none" stroke="#fff" stroke-width=".9"/>
        </svg>
      </li>
    </ul>
  </section>

  <section class="card card--back" aria-label="Business card back">
    <div class="brand-mark" aria-hidden="true"></div>
    <p class="brand-name">By Karel Voss</p>
  </section>

</main>
</body>
</html>
```